A new PowerPoint Template for a French consulting company

Who are we?

Formed in 2005, Quorv is a consulting company specialising in the human aspect of change and transformation.

From our offices in the heart of Paris, our team of 30 consultants work with leading organisations in the Aerospace, Finance, Transportation and Public sectors to deliver lasting change.

Our customers trust us with some of their most strategic and sensitive projects. They trust us with these projects because:
- We listen to them, ensuring we understand the real needs of their business
- We involve them, co-developing and tailoring our solutions to the specific challenges they face
- We’re professional, without taking ourselves too seriously
- We’re imaginative, whilst always remaining pragmatic
- We get results!

You can find out more about who we are and the work we do here: http://www.quorv-example.fr/en

What we need from you?

We’re approaching our 10th birthday and, whilst we still love what we do, we think it’s the right time to update our image.

We’d like you to design us a new PowerPoint template, that will be used for all of our internal and client facing work. You can base your submissions on our existing logo and colour scheme (see files attached) or you can submit your own fresh ideas – after all, we’re not afraid of change!

Finally, whilst we’re looking for you to be creative, there are some simple guidelines that we need you to keep in mind:

1. The Template needs to include both a front cover and a “content” page

2. The front cover needs to:
- Include our logo
- Reflect “who we are” and the type of work that we do

3. The content page needs to:
- Have a predominantly white background
- Be practical to use, making an effective use of the 4:3 standard PPT size
- Include an area across the top of the page for the slide title
- Include areas along the bottom of the page for the page number and date

4. If you decide to propose a new colour scheme, it should be balanced and the “accents” usable

5. The PowerPoint Template needs to be “printer friendly”

6. The fonts you use should be standard

What we don’t want?

To give you as much help as possible, here are some things that we really don’t want:

- Submissions that are dull grey or navy blue, suggesting we’re nothing but boring corporate suits
- Submissions that are Lulette pink or too “soft and cuddly”
- Submissions that use lots of stock images of “happy, smiling, consultants”
- Submissions that will be the height of fashion today, but completely out of date next year

```html
<!DOCTYPE html>
<html lang="en">
<head>
<meta charset="utf-8">
<title>Quorv – PowerPoint template: cover and content slide</title>
<link rel="stylesheet" href="https://fonts.googleapis.com/css2?family=Carlito:wght@400;700&display=swap">
<style>
  :root {
    --stage: #e4e1dc;
    --paper: #f3f1ee;
    --plum: #5c1f3e;
    --magenta: #9a2d62;
    --magenta-dark: #8a2a58;
    --magenta-light: #a8457a;
    --teal: #5aa79d;
    --teal-soft: #a9d2cc;
    --band: #5e8b83;
    --ink: #3b2030;
    --white: #ffffff;
  }
  * { box-sizing: border-box; margin: 0; padding: 0; }
  html, body { width: 1200px; height: 675px; overflow: hidden; }
  body {
    background: var(--stage);
    font-family: "Carlito", "Calibri", Arial, sans-serif;
    position: relative;
  }
  .slide {
    position: absolute;
    top: 142px;
    width: 413px;
    height: 291px;
    background: var(--paper);
    overflow: hidden;
    box-shadow: 0 1px 3px rgba(0,0,0,0.18);
  }
  .slide--cover { left: 132px; }
  .slide--content { left: 655px; }
  .slide svg.decor { position: absolute; inset: 0; width: 100%; height: 100%; }

  .brand-name {
    position: absolute;
    color: var(--plum);
    font-weight: 700;
    line-height: 1;
  }

  /* cover */
  .cover-photo { position: absolute; inset: 0; width: 100%; height: 100%; }
  .slide--cover .brand-name { left: 18px; top: 18px; font-size: 28px; }
  .cover-title {
    position: absolute; left: 126px; top: 12px;
    font-size: 19px; font-weight: 700; color: var(--magenta);
  }
  .cover-subtitle {
    position: absolute; left: 108px; top: 36px; width: 305px; height: 17px;
    background: var(--band);
    color: var(--white); font-size: 11px; font-weight: 700;
    padding: 2px 0 0 18px;
  }

  /* content */
  .slide--content .brand-name { left: 5px; top: 17px; font-size: 12px; }
  .slide-title {
    position: absolute; left: 53px; top: 11px;
    font-size: 19px; font-weight: 700; color: var(--magenta);
  }
  .slide-body { position: absolute; left: 52px; top: 54px; color: var(--ink); list-style: none; }
  .lead { font-size: 15px; font-weight: 700; color: var(--teal); margin-bottom: 4px; }
  .bullet { position: relative; line-height: 1.2; }
  .bullet::before { position: absolute; color: var(--magenta); }
  .bullet--1 { font-size: 12px; padding-left: 13px; margin-bottom: 5px; }
  .bullet--1::before { content: "◆"; left: 0; top: 1px; font-size: 8px; }
  .bullet--2 { font-size: 10px; padding-left: 21px; margin-bottom: 5px; }
  .bullet--2::before { content: "–"; left: 13px; }
  .bullet--3 { font-size: 8px; padding-left: 29px; margin-bottom: 4px; }
  .bullet--3::before { content: "–"; left: 21px; }
  .bullet--4 { font-size: 6.5px; padding-left: 33px; }
  .bullet--4::before { content: "-"; left: 30px; }

  .footer {
    position: absolute; left: 0; bottom: 0; width: 100%; height: 23px;
    background: var(--magenta-dark); color: var(--white);
  }
  .footer-date {
    position: absolute; left: 0; top: 0; width: 46px; height: 23px;
    background: var(--magenta-light);
    font-size: 5.5px; line-height: 1.2; text-align: center; padding-top: 5px;
  }
  .footer-note { position: absolute; left: 0; width: 100%; top: 8px; text-align: center; font-size: 5.5px; }
  .footer-page { position: absolute; right: 9px; top: 8px; font-size: 5.5px; }
  .footer-slashes { position: absolute; inset: 0; width: 100%; height: 100%; }
</style>
</head>
<body>

  <section class="slide slide--cover" aria-label="Cover slide">
    <svg class="cover-photo" viewBox="0 0 413 291" preserveAspectRatio="none" role="img"
         aria-label="Photograph of a young man lying on a grey floor, daydreaming under a cloud of colourful paint splashes">
      <defs>
        <linearGradient id="photoTone" x1="0" y1="0" x2="0" y2="1">
          <stop offset="0" stop-color="#ece9e6"/>
          <stop offset="0.2" stop-color="#d7c7d6"/>
          <stop offset="0.4" stop-color="#cfd2b7"/>
          <stop offset="0.65" stop-color="#b3b3b1"/>
          <stop offset="1" stop-color="#8f8f8e"/>
        </linearGradient>
      </defs>
      <polygon points="120,0 413,0 413,291 33,291" fill="url(#photoTone)"/>
    </svg>
    <svg class="decor" viewBox="0 0 413 291" preserveAspectRatio="none" aria-hidden="true">
      <line x1="120" y1="0" x2="33" y2="291" stroke="var(--teal)" stroke-width="2.5"/>
      <line x1="112" y1="30" x2="60" y2="200" stroke="var(--teal-soft)" stroke-width="1"/>
    </svg>
    <div class="brand-name">Quorv</div>
    <h1 class="cover-title">Title goes here</h1>
    <p class="cover-subtitle">And the subtitle goes here…</p>
  </section>

  <section class="slide slide--content" aria-label="Content slide">
    <svg class="decor" viewBox="0 0 413 291" preserveAspectRatio="none" aria-hidden="true">
      <line x1="51" y1="0" x2="2" y2="153" stroke="var(--teal)" stroke-width="2"/>
      <line x1="411" y1="3" x2="367" y2="135" stroke="var(--teal-soft)" stroke-width="1.5"/>
    </svg>
    <div class="brand-name">Quorv</div>
    <h2 class="slide-title">Slide title goes here</h2>
    <ul class="slide-body">
      <li class="lead">First sentence</li>
      <li class="bullet bullet--1">Bullet level 1</li>
      <li class="bullet bullet--2">Bullet level 2</li>
      <li class="bullet bullet--3">Bullet level 3</li>
      <li class="bullet bullet--4">Bullet level 4</li>
    </ul>
    <footer class="footer">
      <div class="footer-date">September 12,<br>2014</div>
      <svg class="footer-slashes" viewBox="0 0 413 23" preserveAspectRatio="none" aria-hidden="true">
        <line x1="53" y1="0" x2="47" y2="23" stroke="var(--paper)" stroke-width="1"/>
        <line x1="58" y1="0" x2="52" y2="23" stroke="var(--paper)" stroke-width="1"/>
        <line x1="390" y1="0" x2="384" y2="23" stroke="var(--paper)" stroke-width="1"/>
      </svg>
      <div class="footer-note">Of course we also have a footer</div>
      <div class="footer-page">2</div>
    </footer>
  </section>

</body>
</html>
```